Update Old OR create new Website

Current Website is looking a bit old, I did this one a few years back.

Would like a fresh new look, current website sitepress theme is " the Vanta theme" from plumcrate and I just purchased this theme - "bravlo" also from plumcrate, I quite like the look of - http://bravlo.quorvex-skins.com/tech-business/ and if we could get somthing simlar would be great.

current website is at http://www.hle.com.au, have been playing around with the slider that i like.

I have said 5 pages to be designed but really it is just a 5 page website where most pages will look the same.

Any questions please let me know

Target Market(s)

Business

Coding

Coded - Design and coding required

Number of Pages Required

5+ page

Font styles to use
Sans Serif

Colors
33a6d7
0292cd
ffffff
0255a3

Requirements
Must have
• Device compatibility - pc, tablet, phone
Nice to have
• video
Should not have
• vunerabilities. Must also use images that will expire or disappear, ie must be uploaded to site not links to elsewhere.

```html
<!DOCTYPE html>
<html lang="en">
<head>
<meta charset="utf-8">
<title>HLE Technologies – Whatever IT Takes</title>
<link rel="stylesheet" href="https://fonts.googleapis.com/css2?family=Jost:wght@300;400;500&family=Lato:wght@400;700&display=swap">
<style>
:root{
  --cyan:#00a9d9;
  --cyan-dark:#0292cd;
  --navy:#0255a3;
  --ink:#111;
  --text:#444;
  --line:#dcdcdc;
  --panel:#f3f3f3;
  --footer:#231f20;
  --white:#fff;
}
*{box-sizing:border-box;margin:0;padding:0}
html,body{width:1200px;height:2786px;overflow:hidden}
body{position:relative;background:var(--white);font-family:"Lato",sans-serif;color:var(--text)}
.abs{position:absolute}
.heading{font-family:"Jost",sans-serif;font-weight:400;color:var(--ink)}

/* top bar */
.topbar{left:0;top:0;width:1200px;height:37px;background:var(--cyan);color:var(--white);font-size:13px}
.topbar .item{position:absolute;top:11px;display:flex;align-items:center;gap:7px}

/* nav */
.nav{left:0;top:37px;width:1200px;height:84px;background:var(--white);border-bottom:1px solid #e4e4e4;box-shadow:0 2px 4px rgba(0,0,0,.05)}
.brand{position:absolute;left:121px;top:26px;display:flex;align-items:center;gap:8px;font-family:"Jost",sans-serif;font-size:19px;font-weight:500;color:var(--navy)}
.brand .mark{width:28px;height:28px;background:var(--cyan)}
.nav a{position:absolute;top:33px;font-family:"Jost",sans-serif;font-size:14px;color:#222;text-decoration:none}
.nav a.active{color:var(--cyan)}

/* hero */
.hero{left:0;top:121px;width:1200px;height:486px;
  background:
    radial-gradient(ellipse 200px 260px at 1080px 330px,rgba(30,44,70,.85),rgba(30,44,70,0) 100%),
    radial-gradient(ellipse 170px 200px at 900px 300px,rgba(235,238,242,.95),rgba(235,238,242,0) 100%),
    radial-gradient(ellipse 120px 140px at 880px 150px,rgba(214,178,150,.7),rgba(214,178,150,0) 100%),
    radial-gradient(ellipse 120px 140px at 1010px 140px,rgba(200,160,130,.7),rgba(200,160,130,0) 100%),
    radial-gradient(ellipse 130px 150px at 760px 200px,rgba(190,150,125,.55),rgba(190,150,125,0) 100%),
    radial-gradient(ellipse 300px 120px at 780px 430px,rgba(250,250,250,.9),rgba(250,250,250,0) 100%),
    linear-gradient(90deg,#5f6f7e 0%,#8c9aa7 28%,#c5ced6 52%,#e9edf0 70%,#f4f6f7 100%)}
.hero-title{left:158px;top:294px;font-family:"Jost",sans-serif;font-weight:300;font-size:34px;color:var(--white)}
.hero-rule{left:158px;top:352px;width:42px;height:2px;background:var(--white)}
.hero-text{left:158px;top:371px;width:400px;font-size:12px;line-height:16.5px;color:var(--white)}
.btn-solid{display:flex;align-items:stretch;height:32px;background:var(--cyan);color:var(--white);font-family:"Jost",sans-serif;font-size:12px;font-weight:500;letter-spacing:.5px}
.btn-solid .label{padding:0 12px;display:flex;align-items:center}
.btn-solid .arrow{width:32px;border-left:1px solid rgba(255,255,255,.5);display:flex;align-items:center;justify-content:center}
.btn-line{display:flex;align-items:stretch;height:30px;border:1px solid #bbb;color:#222;font-family:"Jost",sans-serif;font-size:12px;font-weight:400;background:var(--white)}
.btn-line .label{padding:0 15px;display:flex;align-items:center}
.btn-line .arrow{width:30px;border-left:1px solid #bbb;display:flex;align-items:center;justify-content:center}

/* feature cards */
.feature{top:659px;width:225px;height:241px;border:1px solid var(--line);background:var(--white);text-align:center;padding:0 18px}
.feature .icon{margin:36px auto 0;width:52px;height:50px}
.feature h3{font-family:"Jost",sans-serif;font-weight:400;font-size:16px;color:var(--ink);margin-top:16px}
.feature p{font-size:11.5px;line-height:19px;color:#333;margin-top:6px}
.feature.highlight{background:var(--cyan);border-color:var(--cyan);color:var(--white);padding-top:50px}
.feature.highlight p{color:var(--white);margin-top:0}
.feature .btn-outline{display:inline-block;margin-top:22px;border:2px solid var(--white);color:var(--white);font-family:"Jost",sans-serif;font-size:11.5px;padding:5px 16px}

/* support */
.support{left:0;top:954px;width:1200px;height:400px;background:var(--panel)}
.support-photo{left:176px;top:954px;width:298px;height:400px;border-radius:44% 44% 0 0;
  background:
    radial-gradient(ellipse 80px 95px at 150px 110px,#e2c0a6,rgba(226,192,166,0) 100%),
    radial-gradient(ellipse 140px 200px at 150px 300px,#d9b79f 0%,rgba(217,183,159,0) 70%),
    linear-gradient(180deg,#5a3d2c 0%,#7a5641 22%,#caa68c 45%,#7d8288 70%,#676c72 100%)}
.support-title{left:507px;top:1032px;width:520px;font-size:30px;line-height:38px}
.support-text{left:507px;top:1128px;width:500px;font-size:12.5px;line-height:19px;color:#222}

/* web services */
.web{left:0;top:1354px;width:1200px;height:488px;background:linear-gradient(135deg,#0db0dd 0%,#00a6d6 50%,#0399cb 100%);overflow:hidden}
.web-title{position:absolute;left:0;width:1200px;top:32px;text-align:center;font-family:"Jost",sans-serif;font-weight:400;font-size:28px;color:var(--white)}
.web-rule{position:absolute;left:581px;top:80px;width:38px;height:2px;background:var(--white)}
.web svg text{font-family:"Jost",sans-serif;font-size:19px;fill:var(--white)}

/* apps */
.section-title{left:0;width:1200px;text-align:center;font-size:28px}
.title-rule{width:42px;height:2px;background:var(--ink)}
.app{top:1983px;width:225px;height:296px;background:var(--white);border-bottom:3px solid var(--ink);box-shadow:0 0 6px rgba(0,0,0,.08);text-align:center}
.app.current{border-bottom-color:var(--cyan)}
.app .media{height:130px;margin:4px 4px 0}
.app .badge{position:absolute;left:88px;top:-25px;width:48px;height:48px;background:#222;display:flex;align-items:center;justify-content:center}
.app.current .badge{background:var(--cyan)}
.app h3{font-family:"Jost",sans-serif;font-weight:400;font-size:15px;color:var(--ink);margin-top:18px}
.app p{font-size:11px;line-height:13px;color:#555;margin:8px 22px 0}
.app .btn-line{position:absolute;left:50px;top:240px}
.app.current .btn-line{border-color:var(--cyan);background:var(--cyan);color:var(--white)}
.app.current .btn-line .arrow{border-color:rgba(255,255,255,.6)}

/* partners */
.partner{top:2330px;width:126px;height:60px;border:1px solid #e2e2e2;display:flex;align-items:center;justify-content:center;gap:6px;font-family:"Jost",sans-serif;font-size:17px;font-weight:500;color:#333}
.partner .dot{width:12px;height:12px;background:#555;border-radius:50%}

/* footer */
.footer{left:0;top:2443px;width:1200px;height:343px;background:var(--footer);color:#ccc}
.footer h4{position:absolute;top:52px;font-family:"Jost",sans-serif;font-weight:400;font-size:15px;color:var(--white)}
.footer .divider{position:absolute;top:55px;width:1px;height:200px;background:#3a3637}
.quick{position:absolute;left:121px;top:100px;list-style:none;font-size:11.5px;color:#ddd}
.quick li{height:31.5px}
.quick li::before{content:"›";margin-right:9px;color:#aaa}
.contact{position:absolute;left:325px;top:100px;font-size:11.5px;line-height:16px;color:#bbb}
.contact .row{display:flex;gap:10px;margin-bottom:18px}
.contact strong{color:var(--white);font-weight:700}
.map{position:absolute;left:596px;top:103px;width:227px;height:130px;border:2px solid #eee;
  background:
    radial-gradient(ellipse 70px 40px at 175px 95px,#a9cfe6,rgba(169,207,230,0) 100%),
    radial-gradient(ellipse 60px 70px at 30px 40px,#b4d6ea,rgba(180,214,234,0) 100%),
    linear-gradient(135deg,#e8ecdf 0%,#f1efe6 45%,#dfe8d6 70%,#c9e0ec 100%)}
.map svg{position:absolute;left:104px;top:38px}
.field{position:absolute;left:906px;width:173px;background:var(--white);font-size:10px;color:#999;padding:7px 8px}
.submit{position:absolute;left:906px;top:225px;width:83px;height:28px;background:var(--cyan);color:var(--white);font-family:"Jost",sans-serif;font-size:12px;font-weight:500;display:flex;align-items:center;justify-content:center}
.copyright{position:absolute;left:121px;top:313px;font-size:11px;color:#aaa}
.social{position:absolute;top:302px;width:26px;height:26px;border-radius:50%;border:2px solid #fff}
</style>
</head>
<body>

<header class="abs topbar">
  <div class="item" style="left:850px">
    <svg width="12" height="12" viewBox="0 0 24 24"><path fill="#fff" d="M6.6 10.8a15.1 15.1 0 0 0 6.6 6.6l2.2-2.2c.3-.3.7-.4 1-.2 1.1.4 2.3.6 3.6.6.6 0 1 .4 1 1V20c0 .6-.4 1-1 1C10.6 21 3 13.4 3 4c0-.6.4-1 1-1h3.5c.6 0 1 .4 1 1 0 1.3.2 2.5.6 3.6.1.3 0 .7-.2 1z"/></svg>
    <span>1300 555 014</span>
  </div>
  <div class="item" style="left:966px">
    <svg width="14" height="11" viewBox="0 0 24 18"><rect x="1" y="1" width="22" height="16" fill="#fff"/><path d="M1 1l11 9 11-9" fill="none" stroke="#00a9d9" stroke-width="2"/></svg>
    <span>info@hle.com.au</span>
  </div>
</header>

<nav class="abs nav">
  <div class="brand"><span class="mark"></span>HLE Technologies</div>
  <a class="active" style="left:480px">Home</a>
  <a style="left:605px">Our Services ⌄</a>
  <a style="left:771px">Web</a>
  <a style="left:891px">APP’s</a>
  <a style="left:1012px">Contact Us</a>
</nav>

<section class="abs hero" role="img" aria-label="Photo of three smiling colleagues working together around a laptop in a bright office"></section>
<h1 class="abs hero-title">WhateverIT TAKES</h1>
<div class="abs hero-rule"></div>
<p class="abs hero-text">With over a decade of experience, HLE Technologies understands the challenges faced by SMEs. So when we design and build networks, support solutions, hardware and software we improve the performance of your organisation.</p>
<div class="abs btn-solid" style="left:158px;top:459px">
  <span class="label">CONTACT US</span>
  <span class="arrow"><svg width="16" height="10" viewBox="0 0 16 10"><path d="M0 5h14M10 1l4 4-4 4" fill="none" stroke="#fff" stroke-width="1.5"/></svg></span>
</div>

<article class="abs feature" style="left:121px">
  <svg class="icon" viewBox="0 0 52 50"><rect x="1" y="1" width="50" height="13" rx="2" fill="#0292cd"/><rect x="1" y="18" width="50" height="13" rx="2" fill="#0292cd"/><rect x="1" y="35" width="50" height="13" rx="2" fill="#0292cd"/><g fill="#fff"><circle cx="8" cy="7.5" r="2"/><circle cx="8" cy="24.5" r="2"/><circle cx="8" cy="41.5" r="2"/><rect x="30" y="6" width="16" height="3"/><rect x="30" y="23" width="16" height="3"/><rect x="30" y="40" width="16" height="3"/></g></svg>
  <h3>Servers</h3>
  <p>HLE Technologies provides the design, support and maintenance for quality I.T Systems for clients to thrive, change and grow.</p>
</article>
<article class="abs feature highlight" style="left:364px">
  <p>HLE team members take great pride in their depth of understanding of their client’s industries and business models.&nbsp; This knowledge</p>
  <span class="btn-outline">READ MORE</span>
</article>
<article class="abs feature" style="left:609px">
  <svg class="icon" viewBox="0 0 52 50"><path d="M14 36h26a9 9 0 0 0 0-18 13 13 0 0 0-25-3 10 10 0 0 0-1 21z" fill="none" stroke="#0292cd" stroke-width="2.5"/><circle cx="24" cy="26" r="5" fill="none" stroke="#0292cd" stroke-width="2.5"/><circle cx="36" cy="42" r="5" fill="none" stroke="#0292cd" stroke-width="2.5"/></svg>
  <h3>Managed IT</h3>
  <p>HLE team members take great pride in their depth of understanding of their client’s industries and business models.&nbsp; This knowledge</p>
</article>
<article class="abs feature" style="left:854px">
  <svg class="icon" viewBox="0 0 52 50"><g fill="none" stroke="#0292cd" stroke-width="2.2"><circle cx="25" cy="24" r="21"/><ellipse cx="25" cy="24" rx="9" ry="21"/><path d="M4 24h42M7 13h36M7 35h36"/></g><path d="M36 32l10 12-5 0 3 5-3 1-3-5-3 3z" fill="#0292cd"/></svg>
  <h3>Internet</h3>
  <p>Having access to the leading providers of Internet in Australia we can determine not only who will give you the fastest connection.</p>
</article>

<section class="abs support"></section>
<div class="abs support-photo" role="img" aria-label="Photo of a smiling customer support agent wearing a headset, arms folded"></div>
<h2 class="abs heading support-title">Need Any Help? Our 5-Star Support Will Help You.</h2>
<p class="abs support-text">Lorem ipsum dolor sit amet, consectetuer adipiscing elit, sed diam nonummy nibh euismod tincidunt ut laoreet dolore magna aliquam erat volutpat. Ut wisi enim ad minim veniam</p>
<div class="abs btn-line" style="left:507px;top:1209px">
  <span class="label">CONTACT US</span>
  <span class="arrow"><svg width="14" height="10" viewBox="0 0 16 10"><path d="M0 5h14M10 1l4 4-4 4" fill="none" stroke="#333" stroke-width="1.4"/></svg></span>
</div>

<section class="abs web">
  <h2 class="web-title">Web</h2>
  <div class="web-rule"></div>
  <svg class="abs" style="left:0;top:0" width="1200" height="488" viewBox="0 0 1200 488">
    <circle cx="600" cy="412" r="232" fill="none" stroke="#fff" stroke-width="5"/>
    <g fill="#00a6d6" stroke="#fff" stroke-width="3">
      <rect x="341" y="385" width="54" height="54"/>
      <rect x="359" y="296" width="54" height="54"/>
      <rect x="409" y="221" width="54" height="54"/>
      <rect x="484" y="171" width="54" height="54"/>
      <rect x="573" y="153" width="54" height="54"/>
      <rect x="662" y="171" width="54" height="54"/>
      <rect x="737" y="221" width="54" height="54"/>
      <rect x="787" y="296" width="54" height="54"/>
      <rect x="805" y="385" width="54" height="54"/>
    </g>
    <g fill="none" stroke="#fff" stroke-width="2">
      <rect x="357" y="402" width="22" height="16"/><path d="M362 424h12"/>
      <circle cx="386" cy="323" r="3"/><circle cx="377" cy="316" r="2"/><circle cx="395" cy="316" r="2"/><circle cx="386" cy="333" r="2"/>
      <rect x="424" y="238" width="24" height="18"/><path d="M429 245h14M429 250h9"/>
      <path d="M500 193h6l12-7v24l-12-7h-6z"/>
      <circle cx="598" cy="178" r="7"/><path d="M603 183l7 7"/>
      <circle cx="689" cy="198" r="9"/><circle cx="689" cy="198" r="4"/>
      <circle cx="764" cy="248" r="10"/><path d="M760 248l4-4 4 4"/>
      <path d="M806 330l14-14 4 4-14 14-5 1z"/>
      <path d="M821 404h22v14h-14l-6 5z"/>
    </g>
    <text x="328" y="419" text-anchor="end">Website Design</text>
    <text x="345" y="330" text-anchor="end">Digital Strategy</text>
    <text x="392" y="242" text-anchor="end">Content</text>
    <text x="392" y="263" text-anchor="end">Management Systems</text>
    <text x="468" y="182" text-anchor="end">Web Marketing</text>
    <text x="600" y="135" text-anchor="middle">SEO</text>
    <text x="732" y="182">Pay Per Click</text>
    <text x="808" y="250">Remarketing</text>
    <text x="854" y="330">Copywriting</text>
    <text x="872" y="411">Social Media</text>
    <text x="872" y="432">Management</text>
    <rect x="511" y="314" width="200" height="96" rx="5" fill="#fff"/>
    <rect x="530" y="351" width="22" height="22" fill="#00a9d9"/>
    <text x="562" y="369" style="fill:#0255a3;font-size:19px;font-weight:500">HLE Technologies</text>
  </svg>
</section>

<h2 class="abs heading section-title" style="top:1888px">APP’s</h2>
<div class="abs title-rule" style="left:579px;top:1933px"></div>

<article class="abs app" style="left:121px">
  <div class="media" role="img" aria-label="Photo of hands arranging cards on a wooden table" style="background:radial-gradient(ellipse 60px 40px at 110px 70px,rgba(240,236,228,.8),rgba(240,236,228,0) 100%),radial-gradient(ellipse 50px 30px at 30px 100px,rgba(205,160,130,.7),rgba(205,160,130,0) 100%),linear-gradient(135deg,#4e4036 0%,#8d7a6a 45%,#b3a393 60%,#4a3d33 100%)"></div>
  <div class="badge"><svg width="22" height="22" viewBox="0 0 22 22"><circle cx="9" cy="9" r="6" fill="none" stroke="#fff" stroke-width="2.2"/><path d="M13.5 13.5l6 6" stroke="#fff" stroke-width="2.5"/></svg></div>
  <h3>Discovery &amp; Strategy</h3>
  <p>Lorem ipsum dolor sit amet, consectetuer adipiscing elit, sed diam nonummy nibh euismod</p>
  <div class="btn-line"><span class="label">READ MORE</span><span class="arrow"><svg width="14" height="10" viewBox="0 0 16 10"><path d="M0 5h14M10 1l4 4-4 4" fill="none" stroke="#333" stroke-width="1.4"/></svg></span></div>
</article>
<article class="abs app current" style="left:364px">
  <div class="media" role="img" aria-label="Photo of a person using a smartphone at a desk with papers" style="background:radial-gradient(ellipse 50px 35px at 90px 75px,rgba(214,170,140,.75),rgba(214,170,140,0) 100%),radial-gradient(ellipse 70px 30px at 160px 105px,rgba(255,255,255,.9),rgba(255,255,255,0) 100%),linear-gradient(135deg,#f3efe9 0%,#e3d9cc 50%,#c8b6a0 100%)"></div>
  <div class="badge"><svg width="22" height="20" viewBox="0 0 22 20"><rect x="2" y="2" width="18" height="12" fill="none" stroke="#fff" stroke-width="2"/><path d="M7 18h8" stroke="#fff" stroke-width="2"/></svg></div>
  <h3>User Experience Design</h3>
  <p>Lorem ipsum dolor sit amet, consectetuer adipiscing elit, sed diam nonummy nibh euismod</p>
  <div class="btn-line"><span class="label">READ MORE</span><span class="arrow"><svg width="14" height="10" viewBox="0 0 16 10"><path d="M0 5h14M10 1l4 4-4 4" fill="none" stroke="#fff" stroke-width="1.4"/></svg></span></div>
</article>
<article class="abs app" style="left:609px">
  <div class="media" role="img" aria-label="Photo of a smartphone in front of a chalkboard sketch of app ideas" style="background:radial-gradient(ellipse 28px 45px at 108px 80px,rgba(220,232,238,.85),rgba(220,232,238,0) 100%),linear-gradient(135deg,#2f2a27 0%,#5c544e 45%,#6d645c 55%,#2a2624 100%)"></div>
  <div class="badge"><svg width="16" height="22" viewBox="0 0 16 22"><rect x="2" y="1" width="12" height="20" rx="2" fill="none" stroke="#fff" stroke-width="2"/><circle cx="8" cy="17" r="1.3" fill="#fff"/></svg></div>
  <h3>Mobile App Development</h3>
  <p>Lorem ipsum dolor sit amet, consectetuer adipiscing elit, sed diam nonummy nibh euismod</p>
  <div class="btn-line"><span class="label">READ MORE</span><span class="arrow"><svg width="14" height="10" viewBox="0 0 16 10"><path d="M0 5h14M10 1l4 4-4 4" fill="none" stroke="#333" stroke-width="1.4"/></svg></span></div>
</article>
<article class="abs app" style="left:854px">
  <div class="media" role="img" aria-label="Photo of two colleagues reviewing work at a computer monitor" style="background:radial-gradient(ellipse 50px 40px at 170px 50px,rgba(150,190,215,.8),rgba(150,190,215,0) 100%),radial-gradient(ellipse 60px 50px at 60px 85px,rgba(40,46,56,.85),rgba(40,46,56,0) 100%),linear-gradient(135deg,#6b7580 0%,#a7b1ba 50%,#414953 100%)"></div>
  <div class="badge"><svg width="22" height="20" viewBox="0 0 22 20"><rect x="2" y="2" width="18" height="12" fill="none" stroke="#fff" stroke-width="2"/><path d="M7 18h8M8 8l2 2 4-4" stroke="#fff" stroke-width="2" fill="none"/></svg></div>
  <h3>Testing &amp; Deployment</h3>
  <p>Lorem ipsum dolor sit amet, consectetuer adipiscing elit, sed diam nonummy nibh euismod</p>
  <div class="btn-line"><span class="label">READ MORE</span><span class="arrow"><svg width="14" height="10" viewBox="0 0 16 10"><path d="M0 5h14M10 1l4 4-4 4" fill="none" stroke="#333" stroke-width="1.4"/></svg></span></div>
</article>

<div class="abs partner" style="left:121px">Ledgerline</div>
<div class="abs partner" style="left:260px">Cricketfield</div>
<div class="abs partner" style="left:399px">nodeforge</div>
<div class="abs partner" style="left:538px"><span class="dot"></span>Tessaro</div>
<div class="abs partner" style="left:677px">Vaulten</div>
<div class="abs partner" style="left:816px"><span class="dot"></span>Leadmost</div>
<div class="abs partner" style="left:955px"><span class="dot"></span>Corvane</div>

<footer class="abs footer">
  <h4 style="left:121px">QUICK LINKS</h4>
  <h4 style="left:325px">CONTACT DETAILS</h4>
  <h4 style="left:596px">LOCATION MAP</h4>
  <h4 style="left:908px">CONTACT NOW</h4>
  <span class="divider" style="left:282px"></span>
  <span class="divider" style="left:553px"></span>
  <span class="divider" style="left:869px"></span>
  <ul class="quick">
    <li>Home</li><li>Our Services</li><li>Web</li><li>App’s</li><li>Contact Us</li>
  </ul>
  <div class="contact">
    <div class="row">
      <svg width="11" height="15" viewBox="0 0 12 16"><path d="M6 0a6 6 0 0 0-6 6c0 4.5 6 10 6 10s6-5.5 6-10a6 6 0 0 0-6-6zm0 8.5A2.5 2.5 0 1 1 6 3.5a2.5 2.5 0 0 1 0 5z" fill="#fff"/></svg>
      <div><strong>HLE Technologies<br>Informationtechnology</strong><br><span style="display:block;margin-top:6px">12 Harbour Lane,<br>Eastfield</span></div>
    </div>
    <div class="row" style="color:#fff;font-weight:700">
      <svg width="12" height="12" viewBox="0 0 24 24"><path fill="#fff" d="M6.6 10.8a15.1 15.1 0 0 0 6.6 6.6l2.2-2.2c.3-.3.7-.4 1-.2 1.1.4 2.3.6 3.6.6.6 0 1 .4 1 1V20c0 .6-.4 1-1 1C10.6 21 3 13.4 3 4c0-.6.4-1 1-1h3.5c.6 0 1 .4 1 1 0 1.3.2 2.5.6 3.6.1.3 0 .7-.2 1z"/></svg>
      <span>1300 555 014</span>
    </div>
    <div class="row">
      <svg width="13" height="10" viewBox="0 0 24 18"><rect x="1" y="1" width="22" height="16" fill="#fff"/><path d="M1 1l11 9 11-9" fill="none" stroke="#231f20" stroke-width="2"/></svg>
      <span>info@hle.com.au</span>
    </div>
  </div>
  <div class="map" role="img" aria-label="Street map showing the office location">
    <svg width="16" height="22" viewBox="0 0 12 16"><path d="M6 0a6 6 0 0 0-6 6c0 4.5 6 10 6 10s6-5.5 6-10a6 6 0 0 0-6-6zm0 8.5A2.5 2.5 0 1 1 6 3.5a2.5 2.5 0 0 1 0 5z" fill="#e0342b"/></svg>
  </div>
  <div class="field" style="top:101px;height:28px">Your Name</div>
  <div class="field" style="top:135px;height:28px">Your Email</div>
  <div class="field" style="top:169px;height:46px">Message</div>
  <div class="submit">SUBMIT</div>
  <p class="copyright">Copyright © 2017 HLE Technologies Informationtechnology. All Rights Reserved.</p>
  <span class="social" style="left:940px;background:#3b5998"></span>
  <span class="social" style="left:975px;background:#0e76a8"></span>
  <span class="social" style="left:1010px;background:#1da1f2"></span>
  <span class="social" style="left:1045px;background:#dd4b39"></span>
</footer>

</body>
</html>
```